Label Redesign For Hemp Oil Tincture Bottle*

I need a label redesigned for Marbleleaf Hemp, current bottle label and logo is attached. The current label doesn't standout, not sure if its the font size or colors on the existing label. It is very important to have on the label that this is a Premium Full Spectrum Hemp Oil that is 2000mg. Then after the label is redesigned and approved, I would need to packaging to be designed to match the approved label design.
This Hemp oil has a relaxing effect to help ease mental and emotional stress, tension and worry. The Omega Fatty Acids it contains also naturally improves your mood and overall brain function, causing you to feel more alert and focused. Hemp Oil helps with insomnia. Take some 2-3 hours before bedtime, you will feel relaxed yet aware of how tired you are that it will lead to a good night's sleep. Hemp Oil helps ease chronic pain and inflammation from conditions such as arthritis, fibromyalgia, lupus, and MS. As a pain relief supplement, it is a safer, natural, non-chemical and non-addictive alternative to prescription painkillers.

Target Market(s)

Adults

Industry/Entity Type

Supplement

Font styles to use
Serif
Sans Serif

Colors

Designer to choose colors to be used in the design.

Requirements
Must have
• All information thats on current label but where it says 750 in the front of the existing label, it needs to say 2000. The 2000 should be prominent on the label.

```html
<!DOCTYPE html>
<html lang="en">
<head>
<meta charset="utf-8">
<title>Marbleleaf Hemp – Full-Spectrum 2000mg Package</title>
<link rel="stylesheet" href="https://fonts.googleapis.com/css2?family=Libre+Baskerville:ital,wght@0,400;0,700;1,400;1,700&display=swap">
<style>
  :root {
    --backdrop: #749676;
    --panel-white: #ffffff;
    --brand-green: #3f7d43;
    --green-light: #55ad55;
    --green-dark: #2c7a31;
    --silver-light: #f1f2f3;
    --silver-mid: #b9bcbf;
    --silver-dark: #8e9296;
    --text-light: #ffffff;
    --text-dark: #1c1c1c;
  }
  * { margin: 0; padding: 0; box-sizing: border-box; }
  html, body { width: 1200px; height: 900px; overflow: hidden; }
  body {
    position: relative;
    background: var(--backdrop);
    font-family: "Libre Baskerville", "Times New Roman", serif;
  }
  .package { position: absolute; top: 30px; left: 315px; width: 570px; height: 840px; display: flex; }
  .panel { position: relative; height: 840px; background: var(--panel-white); overflow: hidden; }
  .panel-side { width: 230px; border-right: 1px solid rgba(0,0,0,0.12); }
  .panel-front { width: 340px; }
  .panel-shapes { position: absolute; inset: 0; }

  /* side panel */
  .side-brand { position: absolute; top: 40px; left: 0; width: 100%; text-align: center; color: var(--brand-green); }
  .side-brand .brand-dot { width: 40px; height: 40px; margin: 0 auto 18px; }
  .side-brand .brand-name { font-size: 28px; }
  .side-info {
    position: absolute; top: 390px; left: 18px; right: 18px;
    color: var(--text-light); font-size: 10.5px; line-height: 1.5;
  }
  .side-info p + p { margin-top: 16px; }
  .side-info strong { font-weight: 700; }
  .side-storage { font-weight: 700; text-transform: uppercase; font-size: 9.5px; letter-spacing: 0.02em; }

  /* shared brand */
  .brand-dot { display: block; border-radius: 50%; background: var(--brand-green); }
  .brand-name { font-weight: 700; line-height: 1.2; }

  /* front panel */
  .front-brand { position: absolute; top: 50px; left: 0; width: 100%; text-align: center; color: var(--brand-green); }
  .front-brand .brand-dot { width: 54px; height: 54px; margin: 0 auto 22px; }
  .front-brand .brand-name { font-size: 38px; }
  .leaf-decoration {
    position: absolute; left: 40px; top: 500px; width: 240px; height: 240px; border-radius: 50%;
    background: radial-gradient(circle, rgba(255,255,255,0.16) 0%, rgba(255,255,255,0) 70%);
  }
  .claims { position: absolute; top: 418px; left: 0; width: 100%; text-align: center; color: var(--text-light); }
  .claim-premium { font-style: italic; font-weight: 700; font-size: 27px; }
  .claim-spectrum { font-style: italic; font-weight: 700; font-size: 20px; margin-top: 4px; }
  .claim-strength { font-size: 24px; margin-top: 20px; }
  .thc-note { position: absolute; top: 588px; right: 26px; color: var(--text-light); font-size: 22px; line-height: 1.2; text-align: center; }
  .product-type { position: absolute; top: 680px; left: 0; width: 100%; text-align: center; color: var(--text-light); }
  .product-category { font-size: 18px; }
  .product-flavor { font-size: 17px; font-weight: 700; margin-top: 6px; }
  .volume-tag {
    position: absolute; bottom: 0; left: 50%; transform: translateX(-50%);
    padding: 14px 22px 12px; background: var(--panel-white); border-radius: 16px 16px 0 0;
    color: var(--text-dark); font-weight: 700; font-size: 16px; white-space: nowrap;
  }
</style>
</head>
<body>
  <main class="package">
    <section class="panel panel-side">
      <svg class="panel-shapes" width="230" height="840" viewBox="0 0 230 840" aria-hidden="true">
        <defs>
          <linearGradient id="silverSide" x1="0" y1="0" x2="1" y2="0">
            <stop offset="0" stop-color="var(--silver-light)"/>
            <stop offset="0.5" stop-color="var(--silver-mid)"/>
            <stop offset="1" stop-color="var(--silver-dark)"/>
          </linearGradient>
          <linearGradient id="greenSide" x1="0" y1="0" x2="1" y2="1">
            <stop offset="0" stop-color="var(--green-dark)"/>
            <stop offset="0.6" stop-color="var(--green-light)"/>
            <stop offset="1" stop-color="var(--green-dark)"/>
          </linearGradient>
        </defs>
        <path d="M0 300 L 230 318 L 230 372 L 0 352 Z" fill="url(#silverSide)"/>
        <path d="M0 352 L 230 372 L 230 840 L 0 840 Z" fill="url(#greenSide)"/>
      </svg>
      <header class="side-brand">
        <span class="brand-dot"></span>
        <div class="brand-name">Marbleleaf<br>Hemp</div>
      </header>
      <div class="side-info">
        <p><strong>Suggested Use:</strong> Shake well. Place one dropper under the tongue, hold briefly, then swallow. Use daily.</p>
        <p>Serving Size: 1 dropper (1 ml)<br>Servings Per Container: 30<br>Hemp Extract per serving: 66 mg</p>
        <p>Warning: Consult your physician before use if pregnant, nursing or taking medication. Keep out of reach of children.</p>
        <p class="side-storage">Store in a cool dry place</p>
      </div>
    </section>

    <section class="panel panel-front">
      <svg class="panel-shapes" width="340" height="840" viewBox="0 0 340 840" aria-hidden="true">
        <defs>
          <linearGradient id="silverBand" x1="0" y1="0" x2="1" y2="0">
            <stop offset="0" stop-color="var(--silver-dark)"/>
            <stop offset="0.3" stop-color="var(--silver-light)"/>
            <stop offset="0.6" stop-color="var(--silver-mid)"/>
            <stop offset="1" stop-color="var(--silver-light)"/>
          </linearGradient>
          <linearGradient id="greenField" x1="0" y1="0" x2="1" y2="1">
            <stop offset="0" stop-color="var(--green-dark)"/>
            <stop offset="0.55" stop-color="var(--green-light)"/>
            <stop offset="1" stop-color="var(--green-dark)"/>
          </linearGradient>
        </defs>
        <path d="M0 318 C 90 340, 200 300, 340 268 L 340 330 C 200 350, 100 390, 0 372 Z" fill="url(#silverBand)"/>
        <path d="M0 372 C 100 390, 200 350, 340 330 L 340 840 L 0 840 Z" fill="url(#greenField)"/>
      </svg>
      <header class="front-brand">
        <span class="brand-dot"></span>
        <div class="brand-name">Marbleleaf<br>Hemp</div>
      </header>
      <div class="leaf-decoration" role="img" aria-label="Faint hemp leaf decoration"></div>
      <div class="claims">
        <p class="claim-premium">Premium</p>
        <p class="claim-spectrum">Full-Spectrum</p>
        <p class="claim-strength">2000mg</p>
      </div>
      <p class="thc-note">Zero<br>THC</p>
      <div class="product-type">
        <p class="product-category">DIETARY SUPPLEMENT</p>
        <p class="product-flavor">Natural Peppermint Flavor</p>
      </div>
      <p class="volume-tag">1 fl oz (30ml)</p>
    </section>
  </main>
</body>
</html>
```